Business Card for New Business

Please design a business card using our logo and font files. This is only one card for one person, as listed in details section.

Industry/Entity Type

Business

Contact Information for Business Card

Carl Voserby

Phone 240.318.6624
Cell 703.581.4096
Email carl@moltravex.com

www.moltravex.com

Address
18250 Brennick Lane #314
Damascus, MD 20715

Font styles to use
Sans Serif

Requirements
Must have
• Information listed in detail section. Must be standard card size.

```html
<!DOCTYPE html>
<html lang="en">
<head>
<meta charset="utf-8">
<title>Moltravex Productions – Business Card</title>
<link rel="stylesheet" href="https://fonts.googleapis.com/css2?family=Didact+Gothic&display=swap">
<style>
  :root {
    --backdrop: #e6e6e4;
    --card-white: #fbfbfa;
    --card-black: #1d1a19;
    --ink: #3a3a3a;
    --ink-soft: #555555;
    --brand-orange: #c8441e;
    --brand-light: #f2f2f2;
    --card-shadow: 0 10px 28px rgba(0, 0, 0, 0.18);
  }
  * { margin: 0; padding: 0; box-sizing: border-box; }
  html, body {
    width: 1054px;
    height: 1200px;
    overflow: hidden;
    background: var(--backdrop);
    font-family: "Didact Gothic", "Helvetica Neue", Arial, sans-serif;
  }
  .canvas {
    position: relative;
    width: 1054px;
    height: 1200px;
  }
  .card {
    position: absolute;
    left: 87px;
    width: 880px;
    height: 503px;
    box-shadow: var(--card-shadow);
  }
  .card--back {
    top: 62px;
    background: var(--card-black);
    display: flex;
    align-items: center;
    justify-content: center;
  }
  .card--front {
    top: 635px;
    background: var(--card-white);
  }
  .wordmark {
    display: flex;
    align-items: center;
    gap: 14px;
    font-weight: 400;
    letter-spacing: 0.04em;
    white-space: nowrap;
  }
  .wordmark__dot {
    width: 0.62em;
    height: 0.62em;
    border-radius: 50%;
    background: currentColor;
    flex: none;
  }
  .card--back .wordmark {
    color: var(--brand-light);
    font-size: 56px;
  }
  .card--front .wordmark {
    position: absolute;
    left: 64px;
    top: 62px;
    color: var(--brand-orange);
    font-size: 40px;
  }
  .contact {
    position: absolute;
    left: 64px;
    top: 190px;
    color: var(--ink);
  }
  .contact__name {
    font-size: 30px;
    letter-spacing: 0.02em;
    margin-bottom: 22px;
    color: var(--ink);
  }
  .contact__lines {
    list-style: none;
    font-size: 21px;
    line-height: 1.4;
    color: var(--ink-soft);
    letter-spacing: 0.02em;
  }
  .contact__address {
    margin-top: 20px;
    font-style: normal;
    font-size: 21px;
    line-height: 1.4;
    color: var(--ink-soft);
    letter-spacing: 0.02em;
  }
</style>
</head>
<body>
  <main class="canvas">
    <section class="card card--back" aria-label="Business card back">
      <div class="wordmark">
        <span class="wordmark__dot" aria-hidden="true"></span>
        <span class="wordmark__name">Moltravex Productions</span>
      </div>
    </section>

    <section class="card card--front" aria-label="Business card front">
      <div class="wordmark">
        <span class="wordmark__dot" aria-hidden="true"></span>
        <span class="wordmark__name">Moltravex Productions</span>
      </div>
      <div class="contact">
        <p class="contact__name">Carl Voserby</p>
        <ul class="contact__lines">
          <li>240.318.6624</li>
          <li>703.581.4096</li>
          <li>carl@moltravex.com</li>
          <li>www.moltravex.com</li>
        </ul>
        <address class="contact__address">
          18250 Brennick Lane #314<br>
          Larkmoor Falls, QR 20715
        </address>
      </div>
    </section>
  </main>
</body>
</html>
```